Vira Nostalma is a dietary supplement company and in need of label design for 4 products

label for 4 dietary supplement products :1- Biotin. Red bottle ( please see the picture attached, not the whole bottle is colored but rather its a white bottle with the upper part and lower part of the bottle colored)2- COQ10. Orange Bottle 3- Hair Skin Nail. Pink bottle 4- Probiotics. Green Bottle we like the label to:1- have a modern and sleek appearance with very limited graphics.2- have a transparent background( as the bottle is white )3- have the box with the supplement and ingredient to appear sideways( horizontal )4- to have a color matching the bottle color.attached you will find :1- the dimension of the bottle.2- four different labels for each of the products.3- two pictures of the bottles 4- picture of the caps5- Logo
Industry/Entity Type
Health And Wellness
Colors
Designer to choose colors to be used in the design.
Look and feel
Each slider illustrates characteristics of the customer's brand and the style your logo design should communicate.

```html
<!DOCTYPE html>
<html lang="en">
<head>
<meta charset="utf-8">
<title>Vira Nostalma CoQ10 Label</title>
<link rel="stylesheet" href="https://fonts.googleapis.com/css2?family=Oswald:wght@400;500;600&family=Roboto+Condensed:wght@400;700&display=swap">
<style>
  :root {
    --stage: #f4efe9;
    --label-white: #ffffff;
    --brand-orange: #f0531c;
    --orange-soft: #f37a45;
    --ink: #1f1f1f;
    --leaf-green: #7cc242;
  }
  * { margin: 0; padding: 0; box-sizing: border-box; }
  html, body { width: 1200px; height: 787px; overflow: hidden; }
  body {
    background: var(--stage);
    display: flex; align-items: center; justify-content: center;
    font-family: "Roboto Condensed", sans-serif;
  }
  .label {
    position: relative;
    width: 1080px; height: 600px;
    background: var(--label-white);
    box-shadow: 0 6px 24px rgba(0,0,0,.12);
    overflow: hidden;
  }
  .label__waves { position: absolute; inset: 0; }
  .front-panel {
    position: absolute; left: 0; top: 0; width: 640px; height: 600px;
  }
  .brand {
    position: absolute; left: 50%; top: 60px; transform: translateX(-50%);
    display: flex; align-items: center; gap: 10px;
    font-family: "Oswald", sans-serif; font-weight: 500;
    font-size: 34px; color: var(--ink); letter-spacing: .5px;
    white-space: nowrap;
  }
  .brand__mark { width: 14px; height: 14px; background: var(--leaf-green); }
  .product-name {
    position: absolute; left: 0; right: 0; top: 125px; text-align: center;
    font-family: "Oswald", sans-serif; font-weight: 600;
    font-size: 78px; color: var(--brand-orange); letter-spacing: 2px;
  }
  .leaf-art {
    position: absolute; left: 500px; top: 330px; width: 72px; height: 72px;
    border-radius: 10px;
    background: linear-gradient(135deg, rgba(255,255,255,.35), rgba(255,255,255,.12));
  }
  .category {
    position: absolute; left: 0; right: 0; bottom: 62px; text-align: center;
    font-size: 26px; color: var(--brand-orange);
  }
  .net {
    position: absolute; left: 0; right: 0; bottom: 18px; text-align: center;
    font-size: 15px; font-weight: 700; color: var(--brand-orange); line-height: 1.3;
  }
  .facts-panel {
    position: absolute; left: 690px; top: 120px; width: 340px;
    background: var(--label-white);
    border: 3px solid var(--ink); padding: 10px 12px;
    color: var(--ink); font-size: 13px;
  }
  .facts__title {
    font-family: "Oswald", sans-serif; font-weight: 600; font-size: 20px;
    border-bottom: 1px solid var(--ink); padding-bottom: 4px;
  }
  .facts__serving { padding: 4px 0; border-bottom: 6px solid var(--ink); line-height: 1.35; }
  .facts__serving strong { font-weight: 700; }
  .facts__calories {
    display: flex; justify-content: space-between; align-items: baseline;
    font-family: "Oswald", sans-serif; font-weight: 600; font-size: 22px;
    border-bottom: 4px solid var(--ink); padding: 4px 0;
  }
  .facts__dv { text-align: right; font-size: 11px; padding: 3px 0; border-bottom: 1px solid var(--ink); }
  .facts__row {
    display: flex; justify-content: space-between;
    padding: 3px 0; border-bottom: 1px solid var(--ink);
  }
  .facts__row--indent { padding-left: 14px; }
  .facts__row:last-child { border-bottom: none; }
</style>
</head>
<body>
  <main class="label">
    <svg class="label__waves" width="1080" height="600" viewBox="0 0 1080 600" aria-hidden="true">
      <path d="M0 250 C220 330 420 330 640 230 C820 150 960 150 1080 200 L1080 420 C900 500 760 450 640 440 C420 420 220 480 0 440 Z" fill="var(--brand-orange)"/>
      <path d="M0 0 H1080 V30 C900 60 760 40 640 20 C420 -10 200 40 0 20 Z" fill="var(--brand-orange)"/>
    </svg>

    <section class="front-panel">
      <div class="brand"><span class="brand__mark"></span>Vira Nostalma</div>
      <h1 class="product-name">COQ10</h1>
      <div class="leaf-art" role="img" aria-label="Soft leaf illustration"></div>
      <p class="category">Dietary Supplement Products</p>
      <p class="net">NET<br>0.3 OZ (30 Capsules)</p>
    </section>

    <section class="facts-panel">
      <h2 class="facts__title">Nutrition Facts / Næringsinnhold</h2>
      <div class="facts__serving">
        10 servings per container<br>
        <strong>Serving size 1 tea-stick 0.6g (0.02oz)</strong>
      </div>
      <div class="facts__calories"><span>Calories / Energi</span><span>0</span></div>
      <div class="facts__dv">% Daily Value*</div>
      <div class="facts__row"><span>Total Fat / Fett 0g</span><span>0%</span></div>
      <div class="facts__row facts__row--indent"><span>Saturated Fat 0g</span><span>0%</span></div>
      <div class="facts__row facts__row--indent"><span>Trans Fat 0g</span><span></span></div>
      <div class="facts__row"><span>Cholesterol / Kolesterol 0mg</span><span>0%</span></div>
      <div class="facts__row"><span>Sodium / Salt 0mg</span><span>0%</span></div>
      <div class="facts__row"><span>Carbohydrate / Karbohydrater 0g</span><span>0%</span></div>
    </section>
  </main>
</body>
</html>
```